Corporate Business Card Design Project

..Hi designers!
I have established a consultancy within strategic communnications, for which I need a business card design - I've seen some of the things you do in here, and they're great! I'll provide some information in the following:
Name: BrookLedger
Tagline: Guiding Dialogue
Service: Strategic communications consulting (primariy internal communication and optimizing): various organisations - e.g. SMEs, NGOs and NPOs - are offered an analysis of their current efforts and, on the basis of that, management consulting tailored their unique challenges and needs.
It's a sole proprietorship - for now! - but it's my plan to employ 5-20 persons over the years. Therefore the card should NOT symbolize a start-up, but communicate a well-established, serious consultancy. Hence, it should also apply to serious companies and organizations - think Tolvik or Hadley Prewitt Group (both as sender and receiver) ;)
The design should accordingly have a formal, conservative, stylish, corporate, clean look! and ditto colors, eg. black, grey, white etc - corresponding to the logo. The only colour that can appear is the same orange contrast as in my logo (see attachement). Not too bold or dramatic fonds or letters.
I choose the double sided as I think it gives the most professional look: One side with name, titel, phone, e-mail - then a little space - and four additional lines for address.
This composition is if all information should be in the same "column" - feel free to provide suggestions with the address places elsewhere on the one side.
On the other side, I'm only thinkin' something with the logo.
I'd be happy to see different ideas re. the use of the orange contrast, placement of logo, etc.
I do not plan on changing the design of businees cards ever - as I think it is more serious keeping a concept and avoid rebranding - and I'm sure that you can deliver an ever-lasting logo for my company! Thanks :).
Let's play the rest by ear in the correspondance.
Target Market(s)
Executive level: CEOs, HR directors, communication managers/directors, business owners.
Industry/Entity Type
Management Consulting

```html
<!DOCTYPE html>
<html lang="en">
<head>
<meta charset="utf-8">
<title>BrookLedger — Business Card</title>
<link rel="stylesheet" href="https://fonts.googleapis.com/css2?family=Sorts+Mill+Goudy&display=swap">
<style>
  :root {
    --backdrop: #e6e4cf;
    --paper: #f3f3f5;
    --orange: #f79431;
    --ink: #222629;
    --grey: #7d7f82;
    --grey-night: #8a8e91;
    --white: #ffffff;
    --night: #172024;
    --night-deep: #0f1519;
    --serif: "Sorts Mill Goudy", "Goudy Old Style", Georgia, serif;
  }
  * { margin: 0; padding: 0; box-sizing: border-box; }
  html, body { width: 886px; height: 1200px; overflow: hidden; }
  body { background: var(--backdrop); position: relative; font-family: var(--serif); }

  .card { position: absolute; left: 81px; width: 725px; height: 469px; overflow: hidden; }
  .card--front { top: 97px; background: var(--paper); }
  .card--back { top: 636px; background: var(--night); }

  .front__accent { position: absolute; left: 416px; top: 0; width: 309px; height: 100%; background: var(--orange); }

  .lockup { position: absolute; display: inline-block; white-space: nowrap; }
  .lockup__name { display: block; font-size: 46px; line-height: 1; }
  .lockup__tagline { display: block; text-align: right; font-size: 10px; letter-spacing: 2.6px; line-height: 1; margin-top: 2px; }

  .front .lockup { left: 39px; top: 210px; }
  .front .lockup__name { color: var(--ink); }
  .front .lockup__tagline { color: var(--grey); }

  .address { position: absolute; right: 345px; top: 318px; text-align: right; color: var(--grey); font-size: 21px; line-height: 28px; font-style: normal; }

  .holder__name { position: absolute; right: 33px; top: 208px; color: var(--white); font-size: 46px; line-height: 1; white-space: nowrap; }
  .holder__details { position: absolute; right: 33px; top: 350px; text-align: right; color: var(--white); }
  .holder__role { font-size: 23px; line-height: 28px; }
  .holder__line { font-size: 18px; line-height: 28px; display: flex; justify-content: flex-end; align-items: center; gap: 7px; }
  .holder__line svg { width: 12px; height: 12px; }

  .back__diamond { position: absolute; inset: 0; width: 100%; height: 100%; }
  .back .lockup { left: 50%; top: 204px; transform: translateX(-50%); }
  .back .lockup__name { color: var(--white); }
  .back .lockup__tagline { color: var(--grey-night); }
</style>
</head>
<body>
  <section class="card card--front front" aria-label="Card front">
    <div class="front__accent"></div>
    <div class="lockup">
      <span class="lockup__name">BrookLedger</span>
      <span class="lockup__tagline">Guiding Dialogue</span>
    </div>
    <address class="address">
      BrookLedger.com<br>
      72 Lindenlaan,<br>
      1050 Ixelles,<br>
      Belgium
    </address>
    <div class="holder__name">Ivo Laine</div>
    <div class="holder__details">
      <div class="holder__role">Director</div>
      <div class="holder__line">
        <svg viewBox="0 0 12 12" aria-hidden="true"><path d="M3 1 L5 3.5 L4 5 Q5.5 7.5 7 8 L8.5 7 L11 9 L9.5 11 Q4 10.5 1 3 Z" fill="var(--white)"/></svg>
        <span>+32 471 20 86</span>
      </div>
      <div class="holder__line">
        <svg viewBox="0 0 12 12" aria-hidden="true"><circle cx="6" cy="6" r="5" fill="none" stroke="var(--white)" stroke-width="1.2"/><circle cx="6" cy="6" r="2" fill="none" stroke="var(--white)" stroke-width="1.2"/></svg>
        <span>ivo@brookledger.com</span>
      </div>
    </div>
  </section>

  <section class="card card--back back" aria-label="Card back">
    <svg class="back__diamond" viewBox="0 0 725 469" preserveAspectRatio="none" aria-hidden="true">
      <polygon points="362.5,0 725,234.5 362.5,469 0,234.5" fill="var(--night-deep)"/>
    </svg>
    <div class="lockup">
      <span class="lockup__name">BrookLedger</span>
      <span class="lockup__tagline">Guiding Dialogue</span>
    </div>
  </section>
</body>
</html>
```